Namecard design for Forex trading & training company

We need a design for a financial forex trading company.
Namecard should give customer a professional yet premium feel, able to differentiate from others.
1) most financial companies employs white background, while its clean and professional, it is too mainstream.
2) I am thinking of brown as base colour, however it easily gives the perception of being an Interior Design company
3) Task is to find a design that is able to portray a clean professional feel, at the same time, appear premium and differentiated from others.
*I'll be employing 3D textured print for my company namecard just so as to give it a better finishing.
Please find attached for my logo.
Financial

```html
<!DOCTYPE html>
<html lang="en">
<head>
<meta charset="utf-8">
<title>Veltora Capital – Business Card</title>
<link rel="stylesheet" href="https://fonts.googleapis.com/css2?family=Tinos:wght@400&family=Noto+Sans+SC:wght@500&display=swap">
<style>
  :root {
    --page-bg: #ffffff;
    --ink-navy: #26337c;
    --wood-light: #e3dcd3;
    --wood-mid: #d6cdc2;
    --wood-dark: #c9bfb3;
  }
  * { margin: 0; padding: 0; box-sizing: border-box; }
  html, body {
    width: 1200px;
    height: 1200px;
    overflow: hidden;
    background: var(--page-bg);
  }
  .canvas {
    position: relative;
    width: 1200px;
    height: 1200px;
  }
  .card {
    position: absolute;
    left: 214px;
    width: 784px;
    height: 471px;
    overflow: hidden;
    color: var(--ink-navy);
    font-family: "Tinos", "Times New Roman", serif;
  }
  .card--front { top: 83px; }
  .card--back { top: 651px; }
  .card__texture {
    position: absolute;
    inset: 0;
    background:
      linear-gradient(180deg, rgba(255,255,255,0.15) 0%, rgba(0,0,0,0) 40%, rgba(0,0,0,0.04) 100%),
      linear-gradient(100deg, var(--wood-mid) 0%, var(--wood-light) 35%, var(--wood-mid) 65%, var(--wood-dark) 100%);
  }
  .line {
    position: absolute;
    left: 0;
    right: 0;
    text-align: center;
    white-space: nowrap;
  }
  /* Front */
  .brand-mark {
    position: absolute;
    left: 0;
    right: 0;
    top: 150px;
    display: flex;
    justify-content: center;
    align-items: center;
    gap: 18px;
  }
  .brand-mark__dot {
    width: 34px;
    height: 34px;
    border-radius: 50%;
    background: var(--ink-navy);
  }
  .brand-mark__name {
    font-size: 64px;
    letter-spacing: 0.12em;
    line-height: 1;
  }
  .company-name {
    top: 358px;
    font-size: 19px;
    letter-spacing: 0.55em;
    padding-left: 0.55em;
  }
  .front-web {
    top: 434px;
    font-size: 20px;
    letter-spacing: 0.5em;
    padding-left: 0.5em;
    font-weight: 700;
  }
  /* Back */
  .person-name {
    top: 126px;
    font-size: 33px;
    letter-spacing: 0.38em;
    padding-left: 0.38em;
  }
  .person-title {
    top: 170px;
    font-size: 20px;
    letter-spacing: 0.4em;
    padding-left: 0.4em;
  }
  .person-title-cn {
    top: 248px;
    font-family: "Noto Sans SC", sans-serif;
    font-size: 34px;
    letter-spacing: 0.3em;
    padding-left: 0.3em;
  }
  .contact {
    font-size: 21px;
    letter-spacing: 0.48em;
    padding-left: 0.48em;
  }
  .contact--phone { top: 356px; }
  .contact--web { top: 386px; font-weight: 700; }
  .contact--email { top: 415px; font-weight: 700; }
</style>
</head>
<body>
<main class="canvas">
  <section class="card card--front">
    <div class="card__texture" role="img" aria-label="Weathered light whitewashed wood grain texture"></div>
    <div class="brand-mark">
      <span class="brand-mark__dot"></span>
      <span class="brand-mark__name">Veltora</span>
    </div>
    <p class="line company-name">VELTORA CAPITAL</p>
    <p class="line front-web">www.veltoracapital.com</p>
  </section>

  <section class="card card--back">
    <div class="card__texture" role="img" aria-label="Weathered light whitewashed wood grain texture"></div>
    <p class="line person-name">Marcus Lian</p>
    <p class="line person-title">Pantry Manager</p>
    <p class="line person-title-cn" lang="zh">茶水理</p>
    <p class="line contact contact--phone">(86) 555 010 234</p>
    <p class="line contact contact--web">www.veltoracapital.com</p>
    <p class="line contact contact--email">marcus@veltoracapital.com</p>
  </section>
</main>
</body>
</html>
```